New website design for tech company

I want to redesign the current website - https://quorvalent.co/
I want it to keep the same colors/branding but I want it to resemble the look and feel of the following sites
https://www.drelkusa.com/
https://www.munoro.com/
https://www.pulvane.com/global/us/home
https://www.tovinplc.co.uk/

The site layout

Target Market(s)

tech companies

Industry/Entity Type

tech

Number of Pages Required

2 page

Font styles to use
Serif

Colors

Designer to choose colors to be used in the design.

Requirements
Must have
• a nice updated design that looks cutting edge and innovative and the site colors can match the current logo

```html
<!DOCTYPE html>
<html lang="en">
<head>
<meta charset="utf-8">
<title>Quorvalent — Accessible Web Technologies</title>
<link href="https://fonts.googleapis.com/css2?family=Archivo:wght@800;900&family=Lato:wght@400;700&display=swap" rel="stylesheet">
<style>
  :root{
    --ink:#111111;
    --dark:#222222;
    --hero-dark:#1b1d24;
    --light:#f4f5f8;
    --white:#ffffff;
    --muted:#5b5d63;
    --green:#8cc63f;
    --blue:#0254a8;
    --line:#d9dbe0;
  }
  *{box-sizing:border-box;margin:0;padding:0}
  html,body{width:1200px;height:2662px;overflow:hidden}
  body{position:relative;font-family:"Lato",sans-serif;color:var(--ink);background:var(--white)}
  .abs{position:absolute}
  .heading{font-family:"Archivo",sans-serif;font-weight:900;text-transform:uppercase;letter-spacing:.5px}
  .eyebrow{font-size:20px;display:flex;align-items:center;gap:6px}
  .eyebrow .dot{width:14px;height:14px;border-radius:50%;border:2px solid currentColor}
  .link{font-size:12px;font-weight:700;text-transform:uppercase;display:flex;align-items:center;gap:8px;padding-bottom:12px;border-bottom:2px solid currentColor}
  .body-text{font-size:13.5px;line-height:20px;color:var(--muted)}
  .body-text .brand{font-size:20px;color:var(--ink)}

  /* hero */
  .hero{left:0;top:0;width:1200px;height:627px;background:linear-gradient(100deg,#15171d 0%,#1e2230 40%,#3a3f52 70%,#4a4036 100%)}
  .hero-photo{left:0;top:0;width:1200px;height:627px;background:radial-gradient(ellipse at 78% 45%,rgba(120,100,90,.35),transparent 60%)}
  .nav-logo{left:126px;top:22px;font-size:20px;font-weight:700;color:var(--green);display:flex;align-items:center;gap:8px}
  .nav-logo .mark{width:14px;height:14px;border-radius:50%;background:var(--blue)}
  .nav{top:27px;right:122px;display:flex;gap:34px;font-size:12px;color:var(--white);text-transform:uppercase}
  .nav-rule{left:117px;top:67px;width:961px;height:1px;background:rgba(255,255,255,.55)}
  .hero .eyebrow{position:absolute;left:122px;top:185px;color:var(--white);font-size:19px}
  .hero h1{position:absolute;left:122px;top:222px;font-size:42px;line-height:48px;color:var(--white)}
  .hero p{position:absolute;left:122px;top:373px;width:520px;font-size:13px;line-height:20px;color:#d6d7db}
  .hero .link{position:absolute;left:122px;top:469px;color:var(--green)}

  /* about */
  .about{left:0;top:627px;width:1200px;height:213px;background:var(--light)}
  .about .eyebrow{position:absolute;left:122px;top:62px}
  .about h2{position:absolute;left:122px;top:96px;font-size:41px}
  .about .body-text{position:absolute;left:595px;top:60px;width:480px}

  /* mission */
  .mission{left:0;top:840px;width:1200px;height:447px;background:var(--light)}
  .mission-photo{position:absolute;left:0;top:0;width:591px;height:447px;background:linear-gradient(110deg,#dfe9ee 0%,#9fc3d8 35%,#0b3d8a 60%,#071f5c 100%)}
  .mission h3{position:absolute;left:684px;top:78px;font-size:25px}
  .mission p{position:absolute;left:684px;top:126px;width:330px;font-size:16.5px;line-height:25px;color:var(--muted)}
  .mission .link{position:absolute;left:684px;top:343px;color:var(--ink)}

  /* team */
  .team{left:0;top:1287px;width:1200px;height:633px;background:var(--dark);color:var(--white)}
  .team .eyebrow{position:absolute;left:0;width:1200px;top:62px;justify-content:center}
  .team h2{position:absolute;left:0;width:1200px;top:97px;text-align:center;font-size:41px}
  .member{position:absolute;top:186px;width:254px;height:372px;background:var(--blue);text-align:center}
  .member .photo{width:254px;height:274px}
  .member .role{margin-top:19px;font-size:11px;color:#c5d6ee;text-transform:uppercase}
  .member .name{margin-top:4px;font-size:18px}
  .member .socials{margin-top:9px;display:flex;justify-content:center;gap:10px}
  .member .socials span{width:15px;height:15px;border-radius:50%;background:#c9d6ea}
  .member .socials span.alt{background:var(--green)}

  /* services */
  .services{left:0;top:1920px;width:1200px;height:742px;background:var(--white)}
  .services-map{position:absolute;left:260px;top:90px;width:700px;height:400px;border-radius:50%;background:radial-gradient(ellipse,rgba(220,228,238,.45),transparent 70%)}
  .services .eyebrow{position:absolute;left:112px;top:93px}
  .services h2{position:absolute;left:112px;top:127px;font-size:41px}
  .services .body-text{position:absolute;left:584px;top:92px;width:480px}
  .card{position:absolute;top:247px;height:231px;background:var(--white);box-shadow:0 6px 24px rgba(20,30,60,.08);border-radius:4px;padding:20px 12px}
  .card h4{font-size:27px;font-weight:400;line-height:32px}
  .card p{margin-top:24px;font-size:13px;line-height:20px;color:var(--muted)}
  .card .link{margin-top:16px;display:inline-flex;color:var(--ink)}
  .todo{left:0;width:1200px;top:2591px;text-align:center;font-size:13px;font-weight:700}
</style>
</head>
<body>

<section class="abs hero">
  <div class="abs hero-photo" role="img" aria-label="Photo of a smiling woman holding a laptop in an office corridor"></div>
  <div class="abs nav-logo"><span class="mark"></span>Quorvalent</div>
  <nav class="abs nav"><span>About</span><span>Services</span><span>Lab</span><span>Partners</span><span>Contact Us</span></nav>
  <div class="abs nav-rule"></div>
  <div class="eyebrow"><span class="dot"></span>Quorvalent - A subsidiary of Merrow &amp; Co.</div>
  <h1 class="heading">Ubiquitous ADA Compliant<br>Web Technologies to<br>Shift Humanity Forward</h1>
  <p>Lorem ipsum dolor sit amet, consectetur adipiscing elit. Amet proin ut vitae, felis. Mauris aliquet faucibus iaculis dui vitae ullamcorper ac.</p>
  <div class="link">Learn more <svg width="7" height="10" viewBox="0 0 7 10"><path d="M1 1l4 4-4 4" fill="none" stroke="currentColor" stroke-width="1.8"/></svg></div>
</section>

<section class="abs about">
  <div class="eyebrow"><span class="dot"></span>About Us</div>
  <h2 class="heading">Who We Are</h2>
  <p class="body-text"><span class="brand">Quorvalent</span> is a web based Internet and technology agency aimed at serving, educating, and partnering with brands &amp; organizations on how their products and services can advance the disabled community through inclusion and diversity. By integrating strategies, solutions, and practices accommodating all persons, we strive to shift humanity forward with the power of technology.</p>
</section>

<section class="abs mission">
  <div class="mission-photo" role="img" aria-label="Photo of a business handshake overlaid with a glowing blue network"></div>
  <h3 class="heading">Our Mission</h3>
  <p>To increase awareness and opportunities in the personal &amp; professional lives of disabled persons through technology, regardless of gender, age race or socio-economic background</p>
  <div class="link">Learn more <svg width="7" height="10" viewBox="0 0 7 10"><path d="M1 1l4 4-4 4" fill="none" stroke="currentColor" stroke-width="1.8"/></svg></div>
</section>

<section class="abs team">
  <div class="eyebrow"><span class="dot"></span>Our Team</div>
  <h2 class="heading">Meet Our Team</h2>
  <div class="member" style="left:208px">
    <div class="photo" role="img" aria-label="Portrait of the CEO" style="background:linear-gradient(160deg,#eceae8,#6e5a52 60%,#2c4fa0)"></div>
    <div class="role">CEO</div><div class="name">Marisol</div>
    <div class="socials"><span></span><span class="alt"></span><span></span></div>
  </div>
  <div class="member" style="left:472px">
    <div class="photo" role="img" aria-label="Black and white portrait of the COO" style="background:linear-gradient(160deg,#bdbdbd,#6a6a6a 55%,#1e1e1e)"></div>
    <div class="role">COO</div><div class="name">Darren</div>
    <div class="socials"><span></span><span class="alt"></span><span></span></div>
  </div>
  <div class="member" style="left:737px">
    <div class="photo" role="img" aria-label="Placeholder photo of a handshake with a blue network overlay" style="background:linear-gradient(110deg,#dfe9ee,#9fc3d8 35%,#0b3d8a 65%,#071f5c)"></div>
    <div class="role">CO</div><div class="name">Elliot</div>
    <div class="socials"><span></span><span class="alt"></span><span></span></div>
  </div>
</section>

<section class="abs services">
  <div class="services-map" role="img" aria-label="Faint world map backdrop"></div>
  <div class="eyebrow"><span class="dot"></span>Our Services</div>
  <h2 class="heading">What We Do</h2>
  <p class="body-text"><span class="brand">Quorvalent</span> is a web based Internet and technology agency aimed at serving, educating, and partnering with brands &amp; organizations on how their products and services can advance the disabled community through inclusion and diversity. By integrating strategies, solutions, and practices accommodating all persons, we strive to shift humanity forward with the power of technology.</p>
  <div class="card" style="left:111px;width:316px">
    <h4>Web &amp; Digital<br>Accessibility</h4>
    <p>Lorem ipsum dolor sit amet, consectetur adipiscing elit. Amet proin ut vitae, felis. Mauris aliquet faucibus iaculis dui vitae ullamcorper ac.</p>
    <div class="link">Learn more <svg width="7" height="10" viewBox="0 0 7 10"><path d="M1 1l4 4-4 4" fill="none" stroke="currentColor" stroke-width="1.8"/></svg></div>
  </div>
  <div class="card" style="left:458px;width:315px">
    <h4>Software<br>Development</h4>
    <p>Lorem ipsum dolor sit amet, consectetur adipiscing elit. Amet proin ut vitae, felis. Mauris aliquet faucibus iaculis dui vitae ullamcorper ac.</p>
    <div class="link">Learn more <svg width="7" height="10" viewBox="0 0 7 10"><path d="M1 1l4 4-4 4" fill="none" stroke="currentColor" stroke-width="1.8"/></svg></div>
  </div>
  <div class="card" style="left:804px;width:327px">
    <h4>Training &amp;<br>Education</h4>
    <p>Lorem ipsum dolor sit amet, consectetur adipiscing elit. Amet proin ut vitae, felis. Mauris aliquet faucibus iaculis dui vitae ullamcorper ac.</p>
    <div class="link">Learn more <svg width="7" height="10" viewBox="0 0 7 10"><path d="M1 1l4 4-4 4" fill="none" stroke="currentColor" stroke-width="1.8"/></svg></div>
  </div>
</section>

<div class="abs todo">To be completed</div>

</body>
</html>
```